DULESH WEB DESIGN (please use the uploaded photos)

We are looking for a web design that captures the essence of Dulesh: authenticity, connection with nature, and simplicity. We want the page to convey the story of our brand, from its cultural significance to its commitment to quality and authenticity. Additionally, we need to integrate Dulesh's sub-brands, such as BRELO, our line of healthy pecan nut snacks.

Design Objective:
We want our website to be more than just a product showcase: it should be a reflection of our brand identity and a platform that inspires our customers to connect with us on a deeper level.

Company Background:
Dulesh is a company specializing in walnut production, hunting ranch management, and livestock. The name "Dulesh" means "FOUR" in the PIMA dialect, in honor of the Pima communities that once inhabited the ranch. This historical and cultural connection is at the heart of our brand.

Audience Needs and Aspirations:
All our customers share deep emotional needs. They seek authenticity, honesty, and a happy, simple life. They want to reconnect with their natural state, dream, return to simplicity, and renew their hopes.

Brand Archetype:
Inspired by the archetypes of Edith, Dylan Fairbrook, and Innocent, we aim to reflect the need to be oneself, honesty, and authenticity in all aspects.

Brand Objective:
Our mission is to reconnect our customers with their natural state, offering high-quality products that simplify their lives and inspire them to dream and renew their hopes.

Key Design Elements:

Natural and earthy color palette reflecting our connection to nature.
Images and graphics depicting ranch life, walnut production, and the quality of our products.
Clean and easy-to-navigate design to reflect our philosophy of simplicity and honesty.
Seamless and clear integration of sub-brands, such as BRELO.

Organic Women (30-50 years) committed to exercise and healthy diets. Hunters (40-60 years) with a deeply rooted conservative mindset. Prime Men (40-60 years) with high income, power, and status.

• Brother 1816 Printed

• Authenticity and Nature Connection: Reflect the brand's authenticity and connection to nature through design elements. Simplicity and Navigation: Keep the design clean and easy to navigate. Integration of Sub-brands: Seamlessly incorporate sub-brands like BRELO into the design. Quality Imagery: Use high-quality visuals to showcase products and brand essence. Responsive Design: Ensure the website looks and functions well across different devices. Storytelling: Incorporate storytelling to convey the brand's history, values, and culture. Clear CTAs: Include clear calls-to-action to guide visitors towards desired actions.
• I have the dulesh-ranch.example Domain, also I'm working on WIX

```html
<!DOCTYPE html>
<html lang="en">
<head>
<meta charset="utf-8">
<title>BRELO by Dulesh</title>
<link href="https://fonts.googleapis.com/css2?family=Montserrat:wght@600;700;800;900&family=Mulish:wght@400;500;600&family=Jost:wght@400;500&display=swap" rel="stylesheet">
<style>
:root{
  --orange:#f26a2e;
  --ink:#1d1d1d;
  --text:#3a3a3a;
  --grey-bg:#f5f3f3;
  --white:#ffffff;
  --footer:#000000;
  --muted:#e9e6e6;
}
*{margin:0;padding:0;box-sizing:border-box}
html,body{width:1200px;height:3778px;overflow:hidden;background:var(--white)}
body{position:relative;font-family:"Mulish",sans-serif;color:var(--text)}
.abs{position:absolute}
.heading{font-family:"Montserrat",sans-serif;font-weight:900;color:var(--ink);letter-spacing:.5px}
.btn{position:absolute;background:var(--orange);color:var(--white);font-family:"Montserrat",sans-serif;font-weight:800;display:flex;align-items:center;justify-content:center;letter-spacing:.5px}
.rule{position:absolute;height:3px;width:36px;background:var(--ink)}

/* header */
.brand{left:132px;top:30px;font-family:"Montserrat",sans-serif;font-weight:700;font-size:64px;line-height:1;color:var(--ink);letter-spacing:3px}
.brand-sub{left:282px;top:101px;font-family:"Jost",sans-serif;font-size:12px;color:var(--ink)}
.search{left:500px;top:32px;width:211px;height:41px;border:1.5px solid var(--ink);border-radius:10px;font-family:"Jost",sans-serif;font-size:11px;color:#555;padding:12px 0 0 18px}
.search-btn{position:absolute;right:8px;top:7px;width:26px;height:26px;border-radius:50%;background:var(--ink)}
.call{left:742px;top:30px;display:flex;gap:10px;align-items:center}
.call-label{font-family:"Jost",sans-serif;font-size:13px;color:var(--ink)}
.call-num{font-family:"Montserrat",sans-serif;font-weight:700;font-size:17px;color:var(--ink)}
.cart{left:978px;top:32px}
.cart-count{left:1028px;top:36px;width:36px;height:20px;border-radius:10px;background:var(--orange);color:var(--white);font-size:12px;text-align:center;line-height:20px;font-family:"Jost",sans-serif}
.cart-label{left:1032px;top:60px;font-family:"Jost",sans-serif;font-size:13px;color:var(--ink)}
.nav{top:100px;font-family:"Jost",sans-serif;font-size:14px;color:var(--ink);letter-spacing:.3px}
.nav.active{color:var(--orange)}

/* hero */
.tag{left:132px;top:205px;width:132px;height:44px;border:1.5px solid var(--ink);font-family:"Jost",sans-serif;font-size:18px;color:var(--ink);display:flex;align-items:center;justify-content:center}
.hero-title{left:134px;top:286px;font-size:42px;line-height:64px;letter-spacing:0;white-space:nowrap;z-index:2}
.hero-title .accent{color:var(--orange)}
.hero-img{left:520px;top:183px;width:551px;height:426px;border-radius:45%;background:radial-gradient(ellipse at 50% 50%,#9a5f34 0%,#b77a4c 45%,#e9d7c7 75%,#ffffff 100%);z-index:1}

/* specializing */
.section-title{left:0;width:1200px;text-align:center;font-size:30px}
.spec-img{top:808px;width:298px;height:257px}
.spec-label{position:absolute;left:28px;bottom:28px;font-family:"Montserrat",sans-serif;font-weight:700;font-size:17px;line-height:21px;color:var(--white)}
.spec-label::before{content:"";display:block;width:34px;height:2px;background:var(--white);margin-bottom:16px}

/* welcome */
.welcome-band{left:0;top:1138px;width:1200px;height:537px;background:var(--grey-bg)}
.deco-panel{background:linear-gradient(180deg,#f6a679,#f26a2e)}
.welcome-text{left:305px;top:1305px;width:345px;font-size:14.3px;line-height:22.5px;color:var(--text)}
.walnut-img{left:697px;top:1196px;width:367px;height:425px;border-radius:40%;background:radial-gradient(ellipse,#c58b4a 0%,#d9a86a 50%,#f5f3f3 80%)}

/* products */
.card{top:1865px;width:296px;height:522px;background:var(--white);box-shadow:0 6px 22px rgba(0,0,0,.08)}
.card-img{position:absolute;left:50%;transform:translateX(-50%)}
.card-name{position:absolute;top:316px;width:100%;text-align:center;font-family:"Montserrat",sans-serif;font-weight:600;font-size:17px;color:var(--ink)}
.card-desc{position:absolute;top:348px;width:100%;text-align:center;font-size:12.5px;line-height:19px;color:var(--text)}
.card-price{position:absolute;top:402px;width:100%;text-align:center;font-family:"Montserrat",sans-serif;font-weight:600;font-size:18px;color:var(--ink)}
.card .btn{top:441px;left:84px;width:129px;height:37px;font-size:12px}
.view-all{left:503px;top:2442px;width:194px;height:47px;border:2px solid var(--orange);color:var(--orange);font-family:"Montserrat",sans-serif;font-weight:800;font-size:13px;display:flex;align-items:center;justify-content:center;letter-spacing:.5px}

/* vision/mission */
.vm-band{left:0;top:2560px;width:1200px;height:364px;background:var(--grey-bg)}
.vm-box{top:2620px;width:449px;height:249px;background:var(--white);overflow:hidden}
.vm-title{position:absolute;left:46px;top:46px;font-size:28px}
.vm-text{position:absolute;left:46px;top:104px;width:280px;font-size:17.5px;line-height:25.7px;color:var(--text)}
.vm-mark{position:absolute;right:-92px;top:106px;transform:rotate(-90deg);font-family:"Montserrat",sans-serif;font-weight:900;font-size:58px;color:var(--muted);letter-spacing:2px;width:250px;text-align:center}

/* banner */
.banner{left:0;top:2924px;width:1200px;height:480px;background:linear-gradient(180deg,#a84d22 0%,#c8642c 30%,#7a3616 65%,#000000 100%)}
.banner-title{left:134px;top:2996px;font-size:43px;line-height:55px;color:var(--white);letter-spacing:0}

/* footer */
.footer{left:0;top:3404px;width:1200px;height:374px;background:var(--footer)}
.foot-logo{left:132px;top:3490px;display:flex;align-items:center;gap:14px;font-family:"Jost",sans-serif;font-size:50px;color:var(--white);letter-spacing:2px}
.foot-logo span{width:28px;height:28px;background:var(--orange)}
.foot-h{font-family:"Montserrat",sans-serif;font-weight:700;font-size:13.5px;color:var(--white);padding-bottom:10px;border-bottom:2px solid var(--white)}
.foot-item{display:flex;align-items:center;gap:14px;font-size:12px;line-height:16px;color:var(--white)}
.ico{width:22px;height:22px;border-radius:50%;background:var(--white);flex:none;display:flex;align-items:center;justify-content:center}
.menu{left:757px;font-size:12px;line-height:19.3px;color:var(--white)}
.divider{left:129px;top:3664px;width:935px;height:1px;background:#8a8a8a}
.copy{left:0;top:3712px;width:1200px;text-align:center;font-size:11px;color:var(--white)}
.arrow{top:2150px}
</style>
</head>
<body>

<!-- header -->
<div class="abs brand">BRELO</div>
<div class="abs brand-sub">BY DULESH</div>
<div class="abs search">Search Items
  <div class="search-btn"><svg width="26" height="26" viewBox="0 0 26 26"><circle cx="12" cy="12" r="5" fill="none" stroke="#fff" stroke-width="1.6"/><line x1="15.5" y1="15.5" x2="19" y2="19" stroke="#fff" stroke-width="1.6"/></svg></div>
</div>
<div class="abs call">
  <svg width="30" height="30" viewBox="0 0 24 24"><path d="M6.6 10.8a15 15 0 0 0 6.6 6.6l2.2-2.2a1 1 0 0 1 1-.25 11.4 11.4 0 0 0 3.6.57 1 1 0 0 1 1 1V20a1 1 0 0 1-1 1A17 17 0 0 1 3 4a1 1 0 0 1 1-1h3.5a1 1 0 0 1 1 1c0 1.25.2 2.45.57 3.57a1 1 0 0 1-.25 1z" fill="#1d1d1d"/></svg>
  <div><div class="call-label">CALL US</div><div class="call-num">+52 662 555 0148</div></div>
</div>
<svg class="abs cart" width="38" height="34" viewBox="0 0 38 34"><path d="M1 3h6l5 20h20l4-14H9" fill="none" stroke="#1d1d1d" stroke-width="2.4"/><line x1="12" y1="13" x2="34" y2="13" stroke="#1d1d1d" stroke-width="1.5"/><line x1="13" y1="18" x2="33" y2="18" stroke="#1d1d1d" stroke-width="1.5"/><circle cx="14" cy="29" r="2.6" fill="#1d1d1d"/><circle cx="29" cy="29" r="2.6" fill="#1d1d1d"/></svg>
<div class="abs cart-count">0</div>
<div class="abs cart-label">Cart</div>
<div class="abs nav active" style="left:500px">HOME</div>
<div class="abs nav" style="left:574px">ABOUT US</div>
<div class="abs nav" style="left:685px">SERVICES</div>
<div class="abs nav" style="left:789px">PRODUCTS</div>
<div class="abs nav" style="left:905px">BLOG</div>
<div class="abs nav" style="left:983px">CONTACT US</div>

<!-- hero -->
<div class="abs tag">WELCOME</div>
<div class="abs hero-img" role="img" aria-label="Whole pecan nuts in shell with one cracked open"></div>
<h1 class="abs heading hero-title">WE BELIEVE<br>IN THE <span class="accent">POWER</span><br><span class="accent">OF NATURE</span></h1>
<div class="btn" style="left:135px;top:502px;width:158px;height:51px;font-size:18px">SHOP NOW</div>

<!-- specializing -->
<h2 class="abs heading section-title" style="top:692px">WE ARE SPECIALIZING</h2>
<div class="rule" style="left:582px;top:759px"></div>
<div class="abs spec-img" style="left:132px;background:linear-gradient(160deg,#8a6a48,#5b3f26)" role="img" aria-label="Bowl of shelled walnuts beside whole walnuts"><div class="spec-label">WALNUT<br>PRODUCTION</div></div>
<div class="abs spec-img" style="left:451px;background:linear-gradient(180deg,#6f7648,#4a4a2c)" role="img" aria-label="Hunter in orange vest walking through pine forest with a dog"><div class="spec-label">HUNTING RANCH<br>MANAGEMENT</div></div>
<div class="abs spec-img" style="left:770px;background:linear-gradient(170deg,#b8c0c4,#8a5a38 60%,#4a3a30)" role="img" aria-label="Brown cattle feeding in a barn"><div class="spec-label">LIVESTOCK</div></div>

<!-- welcome -->
<div class="abs welcome-band"></div>
<div class="abs deco-panel" style="left:139px;top:1203px;width:96px;height:411px" role="img" aria-label="Decorative orange pepper illustration"></div>
<h2 class="abs heading" style="left:305px;top:1202px;font-size:29px">WELCOME TO BRELO</h2>
<div class="rule" style="left:307px;top:1261px"></div>
<p class="abs welcome-text">We are a family-owned business dedicated to agriculture, which focuses on cultivating the Sonora region's pecan tree. Our goal is to create authentic products that harness the natural benefits of pecans. We believe in connecting with the land and using sustainable practices to grow pecan trees in the fertile soil of Sonora. This allows us to offer high-quality products that showcase the pure goodness of pecans.</p>
<div class="btn" style="left:305px;top:1548px;width:145px;height:46px;font-size:16px">READ MORE</div>
<div class="abs walnut-img" role="img" aria-label="Pile of shelled walnut halves"></div>

<!-- products -->
<h2 class="abs heading section-title" style="top:1745px">OUR PRODUCTS</h2>
<div class="rule" style="left:582px;top:1811px"></div>
<svg class="abs arrow" style="left:56px" width="26" height="48" viewBox="0 0 26 48"><polyline points="22,2 3,24 22,46" fill="none" stroke="#777" stroke-width="2"/></svg>
<svg class="abs arrow" style="left:1118px" width="26" height="48" viewBox="0 0 26 48"><polyline points="4,2 23,24 4,46" fill="none" stroke="#777" stroke-width="2"/></svg>

<div class="abs card" style="left:134px">
  <div class="card-img" style="top:34px;width:64px;height:225px;border-radius:8px;background:linear-gradient(90deg,#3d63b8,#a9c6f2,#4a70c4)" role="img" aria-label="Blue glass bottle of pecan oil"></div>
  <div class="card-name">PECAN OIL</div>
  <div class="card-desc">Premium pecan oil, carefully<br>extracted to retain its natural flavor</div>
  <div class="card-price">$25.99</div>
  <div class="btn">ADD TO CART</div>
</div>
<div class="abs card" style="left:452px">
  <div class="card-img" style="top:38px;width:64px;height:221px;border-radius:8px;background:linear-gradient(90deg,#8a4e38,#c98d72,#8a4e38)" role="img" aria-label="Bronze bottle of pecan beauty oil"></div>
  <div class="card-name">BEAUTY OIL</div>
  <div class="card-desc">Premium pecan oil, carefully<br>extracted to retain its natural flavor</div>
  <div class="card-price">$25.99</div>
  <div class="btn">ADD TO CART</div>
</div>
<div class="abs card" style="left:772px">
  <div class="card-img" style="top:100px;width:190px;height:120px;border-radius:10px 10px 95px 95px;background:linear-gradient(180deg,#e7b99a,#b8683a)" role="img" aria-label="Terracotta bowl filled with pecan flour"></div>
  <div class="card-name">PECAN FLOUR</div>
  <div class="card-desc">Premium pecan oil, carefully<br>extracted to retain its natural flavor</div>
  <div class="card-price">$25.99</div>
  <div class="btn">ADD TO CART</div>
</div>
<div class="abs view-all">VIEW ALL PRODUCTS</div>

<!-- vision & mission -->
<div class="abs vm-band"></div>
<div class="abs vm-box" style="left:132px">
  <div class="vm-mark">VISION</div>
  <h3 class="heading vm-title">VISION</h3>
  <p class="vm-text">To be a company that develops authentic products, services, and experiences that help reconnect with your natural state.</p>
</div>
<div class="abs vm-box" style="left:609px">
  <div class="vm-mark">MISSION</div>
  <h3 class="heading vm-title">MISSION</h3>
  <p class="vm-text">Create innovative products and services that guide individuals toward rediscovering their true purpose.</p>
</div>

<!-- banner -->
<div class="abs banner" role="img" aria-label="Silhouette of a young cowboy holding a lasso against an orange sunset over ranch land"></div>
<h2 class="abs heading banner-title">RECONNECT<br>WITH YOUR<br>NATURAL STATE.</h2>
<div class="btn" style="left:136px;top:3186px;width:185px;height:56px;font-size:19px">CONTACT US</div>

<!-- footer -->
<div class="abs footer"></div>
<div class="abs foot-logo"><span></span>DULESH</div>

<div class="abs" style="left:484px;top:3420px;width:194px">
  <div class="foot-h">CONTACT US</div>
  <div class="foot-item" style="margin-top:24px"><div class="ico"><svg width="10" height="12" viewBox="0 0 10 12"><path d="M5 0a4 4 0 0 1 4 4c0 3-4 8-4 8S1 7 1 4a4 4 0 0 1 4-4z" fill="#000"/><circle cx="5" cy="4" r="1.4" fill="#fff"/></svg></div><div>Camino Nogal 14,<br>83200 Hermosillo</div></div>
  <div class="foot-item" style="margin-top:18px"><div class="ico"><svg width="11" height="11" viewBox="0 0 24 24"><path d="M6.6 10.8a15 15 0 0 0 6.6 6.6l2.2-2.2a1 1 0 0 1 1-.25 11.4 11.4 0 0 0 3.6.57 1 1 0 0 1 1 1V20a1 1 0 0 1-1 1A17 17 0 0 1 3 4a1 1 0 0 1 1-1h3.5a1 1 0 0 1 1 1c0 1.25.2 2.45.57 3.57a1 1 0 0 1-.25 1z" fill="#000"/></svg></div><div>Call Us<br>+52 662 555 0148</div></div>
  <div class="foot-item" style="margin-top:18px"><div class="ico"><svg width="11" height="9" viewBox="0 0 11 9"><rect x="0" y="0" width="11" height="9" rx="1" fill="#000"/><polyline points="0.5,1 5.5,5 10.5,1" fill="none" stroke="#fff" stroke-width="1"/></svg></div><div>E mail Us<br>info@dulesh-ranch.example</div></div>
</div>

<div class="abs" style="left:757px;top:3420px;width:107px"><div class="foot-h">MENU</div></div>
<div class="abs menu" style="top:3469px">Home<br>About Us<br>Services<br>Products<br>Blog<br>Contact Us</div>

<div class="abs" style="left:961px;top:3420px;width:106px">
  <div class="foot-h">FOLLOW US</div>
  <div class="foot-item" style="margin-top:22px;font-size:11.5px"><div class="ico"></div><div>Like us on<br>CIRCLEPAGE</div></div>
  <div class="foot-item" style="margin-top:18px;font-size:11.5px"><div class="ico"></div><div>Follow us on<br>WORKLINK</div></div>
  <div class="foot-item" style="margin-top:18px;font-size:11.5px"><div class="ico"></div><div>Follow us on<br>PHOTOGRAM</div></div>
</div>
<div class="abs deco-panel" style="left:1115px;top:3411px;width:85px;height:315px" role="img" aria-label="Decorative orange pepper illustration"></div>

<div class="abs divider"></div>
<div class="abs copy">Copyright © 2024 All Rights Reserved</div>

</body>
</html>
```